Harlow Ironworks Business Card

We need a business card design for a new small metal fabrication business in rural NSW, Australia.

The business (Harlow Ironworks) is owner operated by a man with the initials KB - much of the branding comes from this name.

Harlow Ironworks designs, engineers, repairs and manufactures a range of custom, quality metal works including vehicle trays, agricultural machinery impliments, trailers, wood splitters, fire pits, furniture etc.

The brand position focuses on custom work of the highest quality.

Business card design should show quality, attention to detail and stand out among a mass of business cards.

Logos are in the files

The grey color may be changed on the logo if required to stand out more.

There is an image attached of a simple card that is liked because it is clean, clear, simple, masculine and effective. It says 'quality'. As most of the work we do is custom it would be good to have the business card speak to this.

Target Market(s)

Rural and regional based Australians. Primarily adult male 25-60 yrs. Primary production / rural / travelling lifestyle.

Industry/Entity Type

Metal Fabrication

Contact Information for Business Card

The words 'custom quality fabrications' would be great somewhere perhaps on the backside (not on the information side)
Name
title
Phone: 0418 539 746 and (02) 6193 4827
email: info@harlowiw.com.au
www.harlowiw.com.au

address (2 lines)

Requirements
Nice to have
• Background colour should be very navy blue or black.
Should not have
• NO orange and blue combinations.
• Navy is OK

```html
<!DOCTYPE html>
<html lang="en">
<head>
<meta charset="utf-8">
<title>Harlow Ironworks Business Card</title>
<link rel="stylesheet" href="https://fonts.googleapis.com/css2?family=Roboto:wght@400;700&display=swap">
<style>
  :root {
    --backdrop: #3b3330;
    --card: #1a1a1a;
    --steel: #a9a9a9;
    --green: #6cc04a;
    --white: #f2f2f2;
    --rule: #5a5a5a;
  }
  * { box-sizing: border-box; margin: 0; padding: 0; }
  html, body {
    width: 1200px; height: 864px; overflow: hidden;
    background: var(--backdrop);
    font-family: "Roboto", Arial, sans-serif;
  }
  .sheet {
    width: 1200px; height: 864px;
    display: flex; align-items: center; justify-content: center; gap: 40px;
  }
  .card {
    width: 560px; height: 320px;
    background: var(--card);
    border-radius: 4px;
    box-shadow: 0 10px 24px rgba(0,0,0,.45);
    position: relative;
  }
  /* front */
  .card--front {
    display: flex; flex-direction: column; align-items: center; justify-content: center;
  }
  .brand {
    display: flex; align-items: center; gap: 14px;
  }
  .brand__square {
    width: 22px; height: 22px; background: var(--green);
  }
  .brand__name {
    color: var(--steel);
    font-weight: 700; font-size: 34px; letter-spacing: 2px;
    text-transform: uppercase;
  }
  .front__tagline {
    margin-top: 14px;
    color: var(--green); font-weight: 700; font-size: 14px; letter-spacing: 4px;
    text-transform: uppercase;
  }
  .front__web {
    margin-top: 22px;
    color: var(--steel); font-size: 15px; letter-spacing: 3px;
  }
  /* back */
  .card--back {
    display: flex; align-items: center;
  }
  .back__brand {
    width: 250px; display: flex; align-items: center; justify-content: center;
  }
  .back__brand .brand__name { font-size: 26px; line-height: 1.15; }
  .back__rule {
    width: 1px; height: 230px; background: var(--rule);
  }
  .contact { padding-left: 22px; }
  .contact__name {
    color: var(--green); font-weight: 700; font-size: 21px; letter-spacing: .5px;
  }
  .contact__title {
    color: var(--white); font-size: 16px; margin-bottom: 12px;
  }
  .contact__list { list-style: none; }
  .contact__item {
    display: flex; align-items: center; gap: 10px;
    color: var(--white); font-size: 15px; line-height: 25px;
  }
  .contact__item--address { align-items: flex-start; line-height: 20px; margin-top: 4px; }
  .contact__item--address .contact__icon { margin-top: 3px; }
  .contact__icon { width: 14px; height: 14px; flex: none; }
</style>
</head>
<body>
<main class="sheet">
  <section class="card card--front">
    <div class="brand">
      <span class="brand__square"></span>
      <span class="brand__name">Harlow Ironworks</span>
    </div>
    <p class="front__tagline">Custom Quality Fabrications</p>
    <p class="front__web">www.harlowiw.com.au</p>
  </section>

  <section class="card card--back">
    <div class="back__brand">
      <span class="brand__name">Harlow<br>Ironworks</span>
    </div>
    <div class="back__rule"></div>
    <div class="contact">
      <p class="contact__name">KIERAN BLAKE</p>
      <p class="contact__title">President</p>
      <ul class="contact__list">
        <li class="contact__item">
          <svg class="contact__icon" viewBox="0 0 14 14"><circle cx="7" cy="7" r="7" fill="var(--green)"/><path d="M4 4h2l1 2-1 1a4 4 0 0 0 2 2l1-1 2 1v2c-4 0-7-3-7-7z" fill="var(--card)"/></svg>
          0418 539 746
        </li>
        <li class="contact__item">
          <svg class="contact__icon" viewBox="0 0 14 14"><circle cx="7" cy="7" r="7" fill="var(--green)"/><path d="M4 4h2l1 2-1 1a4 4 0 0 0 2 2l1-1 2 1v2c-4 0-7-3-7-7z" fill="var(--card)"/></svg>
          (02) 6193 4827
        </li>
        <li class="contact__item">
          <svg class="contact__icon" viewBox="0 0 14 14"><circle cx="7" cy="7" r="7" fill="var(--green)"/><rect x="3.5" y="4.5" width="7" height="5" fill="var(--card)"/><path d="M3.5 4.5 7 7.5l3.5-3" stroke="var(--green)" fill="none"/></svg>
          info@harlowiw.com.au
        </li>
        <li class="contact__item">
          <svg class="contact__icon" viewBox="0 0 14 14"><circle cx="7" cy="7" r="7" fill="var(--green)"/><circle cx="7" cy="7" r="3.5" fill="none" stroke="var(--card)"/><path d="M3.5 7h7M7 3.5v7" stroke="var(--card)"/></svg>
          www.harlowiw.com.au
        </li>
        <li class="contact__item contact__item--address">
          <svg class="contact__icon" viewBox="0 0 14 14"><circle cx="7" cy="7" r="7" fill="var(--green)"/><path d="M7 11.5 4.3 7.2a3 3 0 1 1 5.4 0z" fill="var(--card)"/><circle cx="7" cy="5.8" r="1" fill="var(--green)"/></svg>
          <span>12 Foundry Lane<br>Bellwater NSW 2731</span>
        </li>
      </ul>
    </div>
  </section>
</main>
</body>
</html>
```